Business Card For Kelmora Financial Consulting

Hi, I would like a business card designed. Bold, modern.
Please use the same design as the logo. I have also attached the website design to see the overall theme.
Wordmark Font
Color: Hex: #01AEF7

```html
<!DOCTYPE html>
<html lang="en">
<head>
<meta charset="utf-8">
<title>Kelmora Financial Consulting – Business Card</title>
<link rel="stylesheet" href="https://fonts.googleapis.com/css2?family=Arimo:ital,wght@0,400;0,700;1,400&display=swap">
<style>
  :root {
    --page-bg: #0b0d0f;
    --card-bg: #141e26;
    --accent: #01aef7;
    --text-light: #ffffff;
    --text-soft: #e6ecf0;
  }
  * { box-sizing: border-box; margin: 0; padding: 0; }
  html, body {
    width: 1200px; height: 963px; overflow: hidden;
    background: var(--page-bg);
    font-family: "Arimo", Arial, sans-serif;
  }
  .card {
    position: absolute; left: 150px; top: 225px;
    width: 900px; height: 514px;
    background: var(--card-bg);
    border-radius: 30px;
    border-bottom: 5px solid var(--accent);
    border-right: 5px solid var(--accent);
    overflow: hidden;
  }
  .brand {
    position: absolute; left: 250px; top: 70px;
    display: flex; align-items: center; gap: 20px;
  }
  .brand-square {
    width: 56px; height: 56px;
    border: 5px solid var(--accent);
  }
  .brand-name {
    color: var(--text-light);
    font-weight: 700; font-size: 30px;
    letter-spacing: 1px; line-height: 1.15;
    text-transform: uppercase;
  }
  .contact {
    position: absolute; left: 70px; top: 215px;
    color: var(--text-soft); font-size: 20px; line-height: 1.45;
  }
  .contact .address { margin-bottom: 14px; }
  .contact-row { display: flex; align-items: center; gap: 12px; }
  .contact-row svg { width: 18px; height: 18px; flex: none; fill: var(--accent); }
  .person {
    position: absolute; right: 60px; top: 215px; text-align: right;
  }
  .person-name {
    color: var(--accent); font-weight: 700; font-size: 28px;
    letter-spacing: 1px; text-transform: uppercase;
  }
  .person-role { color: var(--text-light); font-size: 20px; margin-top: 4px; }
  .edge-tab {
    position: absolute; right: 0; top: 300px;
    width: 14px; height: 46px;
    background: var(--accent);
    border-radius: 6px 0 0 6px;
  }
</style>
</head>
<body>
  <div class="card">
    <div class="brand">
      <div class="brand-square"></div>
      <div class="brand-name">Kelmora Financial<br>Consulting</div>
    </div>

    <div class="contact">
      <p class="address">Your Address<br>City, State, Zip 0000</p>
      <p class="contact-row">
        <svg viewBox="0 0 24 24" aria-hidden="true"><path d="M6.6 10.8a15.1 15.1 0 0 0 6.6 6.6l2.2-2.2c.3-.3.7-.4 1-.2 1.1.4 2.3.6 3.6.6.6 0 1 .4 1 1V20c0 .6-.4 1-1 1A17 17 0 0 1 3 4c0-.6.4-1 1-1h3.5c.6 0 1 .4 1 1 0 1.3.2 2.5.6 3.6.1.3 0 .7-.2 1z"/></svg>
        123-456-2100
      </p>
      <p class="contact-row">
        <svg viewBox="0 0 24 24" aria-hidden="true"><path d="M2 5h20v14H2z M3.5 6.5 12 13l8.5-6.5v-.1H3.5z" fill-rule="evenodd"/></svg>
        youremail@mailbox.com
      </p>
      <p class="contact-row">
        <svg viewBox="0 0 24 24" aria-hidden="true"><path d="M12 2a10 10 0 1 0 0 20 10 10 0 0 0 0-20zm0 2c1.2 1.4 2 3.4 2.2 6H9.8C10 7.4 10.8 5.4 12 4zm-2.2 8h4.4c-.2 2.6-1 4.6-2.2 6-1.2-1.4-2-3.4-2.2-6zM4.1 12h3.7c.1 2.2.6 4.2 1.5 5.6A8 8 0 0 1 4.1 12zm0-2a8 8 0 0 1 5.2-5.6C8.4 5.8 7.9 7.8 7.8 10zm12.1 0c-.1-2.2-.6-4.2-1.5-5.6A8 8 0 0 1 19.9 10zm0 2h3.7a8 8 0 0 1-5.2 5.6c.9-1.4 1.4-3.4 1.5-5.6z"/></svg>
        www.yourwebsite.com
      </p>
    </div>

    <div class="person">
      <p class="person-name">Jonathan Smith</p>
      <p class="person-role">Manager</p>
    </div>

    <div class="edge-tab"></div>
  </div>
</body>
</html>
```